Wireframes of In Store Preview

We need to simplify our in store preview capability. For this particular project what I really need are wireframes for the in store preview form, which is currently several pages - but needs to be condensed. The current Free In-Store Preview process is divided over five pages and is closely tied to the process of purchasing a product. This project simplifies the process and highlights the “no obligation to buy” value proposition of the feature.
Objectives
Simplify the Free In Store Preview (FISP) reservation process. We believe that reducing the number of pages required to complete the reservation process will reduce abandonment. Currently there is a 80+% drop off between the FISP - Edit page and the FISP - Review page. Some of this is to be expected, but we feel that if we can do the following that we can reduce some of that drop-off:
1. highlight the “no obligation to buy” and “see it in person” aspects of FISP
2. Remove the Veltmore Lending option from the payment method form - the CC is only needed to secure the reservation, so having this option here implies that this method is the final form of payment. During the final purchase the customer can choose to use Financing instead.
3. Remove selection of Protection Plan, deferring that to the post-reservation sale, which can provide a better hands-on, concierge experience.
4. reduce the steps from 5 steps to 2.
Here is the current flow:
1. Click Free In Store Preview on the PDP
2. A pop-up displays with the ring size and insurance option - the customer has to choose to preview it again 😔 Edit, Review and then Thank you) to 2 steps (edit/review and then thank you)
3. the form is displayed with the store location and credit card information
4. the review page is displayed on which the customer needs to finalize
5. the thank you page displays
Here is the new flow I’d like to get wireframes for:
* Click Free In Store Preview on the PDP (I don’t need a wireframe for this)
* the form is displayed with the store location and credit card form - once the customer enters their information they can finalize the reservation
* the thank you page displays
I’ve included screenshots of the current flow here. Also - FYI - as an example, I think Dunsel Oakes does a good job of communicating that their Desk Sample Kit option is free even though they do require a credit card authorization to complete the transaction. Also, their core user base is Millenial - just like ours. (I know, you wouldn't know it from our current website! :-) Anyway - I like their cleaner more tech saavy form behavior. So, don't be shy about moving away from the overcrowded multi-step form pages we have now.
Lastly - if you want to try the flow yourself - you can follow these steps:
1. Click here: https://www.bravelle-example.com/engagement-rings/solitaire-diamond-gallery-engagement-ring-in-14kt-white-gold/19815
2. On the setting PDP page here - click the CHOOSE THIS RING button.
3. That will take you to the diamond inventory where you need to select a diamond. Choose any diamond and “add it to your engagement ring” - this will take you to the configured ring PDP
4. Click the FREE IN STORE PREVIEW option on the configured ring PDP - a pop up will display
5. On the pop up, select the ring size (I know, I know - even if you selected one before you’ll need to select it again, this is a bug) and then click the PREVIEW THIS RING button. This will take you to the Free-in-store preview page form.
6. On the free in store preview page, enter a credit card payment method and hit the CONTINUE button. I promise - your card will NOT be charged if you hit this button. This will take you to the Review page.
7. On the Review Page you should STOP. PLEASE DO NOT PROCEED PAST THIS POINT. Please refer to the comp for the thank you page.
Thanks!
Target Market(s)
Millenial Engagement Ring Shoppers
Industry/Entity Type
Store
Number of Pages Required
2 page
Look and feel
Each slider illustrates characteristics of the customer's brand and the style your logo design should communicate.

```html
<!DOCTYPE html>
<html lang="en">
<head>
<meta charset="utf-8">
<title>Reservation Details</title>
<link href="https://fonts.googleapis.com/css2?family=Figtree:wght@400;600&display=swap" rel="stylesheet">
<style>
  :root {
    --maroon: #6b2046;
    --gold: #e0a91f;
    --grey: #858585;
    --label: #7a7a7a;
    --ink: #333333;
    --bg: #ffffff;
  }
  html, body {
    margin: 0;
    padding: 0;
    width: 1098px;
    height: 1200px;
    overflow: hidden;
    background: var(--bg);
    font-family: "Figtree", sans-serif;
  }
  .page { position: relative; width: 1098px; height: 1200px; }
  .abs { position: absolute; margin: 0; line-height: 1; white-space: nowrap; }

  .ring-visual {
    position: absolute; left: 297px; top: 16px; width: 286px; height: 113px;
    background: radial-gradient(ellipse at 50% 55%, #f2f2f4 0%, #d9dadd 55%, #ffffff 100%);
    border-radius: 50%;
  }
  .product-title { color: var(--maroon); font-size: 16px; left: 615px; }

  .spec-label { color: var(--label); font-size: 12px; font-weight: 600; }
  .spec-value { color: var(--grey); font-size: 15.5px; left: 416px; }

  .section-title { color: var(--maroon); font-size: 29px; left: 358px; top: 457px; letter-spacing: 0.3px; }
  .print-link { color: var(--gold); font-size: 13.5px; left: 679px; line-height: 16px; top: 456px; white-space: normal; width: 90px; }

  .field-label { color: var(--label); font-size: 12px; font-weight: 600; }
  .field-large { color: var(--grey); font-size: 22px; }
  .field-value { color: var(--grey); font-size: 15.5px; }
  .note { color: var(--grey); font-size: 12.5px; line-height: 19.5px; left: 362px; top: 769px; width: 360px; white-space: normal; }

  .summary {
    position: absolute; left: 301px; top: 931px; width: 508px; height: 300px;
    border: 2px solid var(--maroon); box-sizing: border-box;
  }
  .line-item { color: var(--ink); font-size: 15.5px; }
  .price { left: 732px; }
  .accent { color: var(--gold); font-size: 14px; }
</style>
</head>
<body>
<main class="page">
  <div class="ring-visual" role="img" aria-label="Product photo of a solitaire diamond engagement ring in white gold"></div>
  <p class="abs product-title" style="top:47px">SOLITAIRE DIAMOND GALLERY</p>
  <p class="abs product-title" style="top:82px">ENGAGEMENT RING</p>

  <p class="abs spec-label" style="left:295px; top:222px">RING</p>
  <p class="abs spec-value" style="top:207px">14KT White Gold (0.10 CTW) in Round Center Stone</p>
  <p class="abs spec-value" style="top:236px">Ring Size 4.75</p>
  <p class="abs spec-label" style="left:297px; top:269px">DIAMOND</p>
  <p class="abs spec-value" style="top:268px">0.62 Carat Diamond (VS2 clarity), Ideal Cut</p>
  <p class="abs spec-value" style="top:297px">Color G</p>

  <h1 class="abs section-title" style="font-weight:400">RESERVATION DETAILS</h1>
  <p class="abs print-link">Print Reservation</p>

  <p class="abs field-label" style="left:361px; top:508px">PREVIEW PERIOD</p>
  <p class="abs field-large" style="left:362px; top:532px">Friday Sept 1 -&nbsp; Tuesday Sept 12</p>

  <p class="abs field-label" style="left:363px; top:582px">PREVIEW LOCATION</p>
  <p class="abs field-large" style="left:363px; top:607px">MARION HALE FINE JEWELERS</p>
  <p class="abs field-large" style="left:363px; top:636px">30, Lorem Avenue, Ipsum Way,</p>
  <p class="abs field-large" style="left:363px; top:665px">Los Angeles, LA90908</p>

  <p class="abs field-label" style="left:363px; top:711px">CONFIRMATION NUMBER</p>
  <p class="abs field-label" style="left:559px; top:711px">RESERVATION STATUS</p>
  <p class="abs field-value" style="left:362px; top:736px">R44E5400Q</p>
  <p class="abs field-value" style="left:559px; top:736px">In Process</p>

  <p class="abs note">Please bring along your identifcation and the credit card used for the reservation so we can confirm your identity.</p>

  <section class="summary" aria-label="Order summary"></section>
  <p class="abs line-item" style="left:350px; top:962px">14KT WHITE GOLD RING</p>
  <p class="abs line-item price" style="top:964px">$ 289</p>
  <p class="abs line-item" style="left:350px; top:992px">O.62 CARAT IDEAL CUT DIAMOND</p>
  <p class="abs line-item price" style="top:990px; left:733px">$ 2750</p>
  <p class="abs line-item" style="left:348px; top:1025px">ITEM TOTAL</p>
  <p class="abs line-item price" style="top:1027px">$ 3049</p>
  <p class="abs line-item" style="left:350px; top:1074px">OVERNGHT SHIPPING&nbsp; <span class="accent">Est. Delivery: 9th Sept.</span></p>
  <p class="abs line-item price" style="top:1074px; left:734px">FREE</p>
  <p class="abs line-item" style="left:349px; top:1104px">W/A SALES TAX (10.0%)</p>
  <p class="abs line-item price" style="top:1102px; left:735px">$ 305</p>
  <p class="abs line-item" style="left:348px; top:1171px">ORDER TOTAL <span class="accent">Fulfilled by Bravelle</span></p>
  <p class="abs line-item price" style="top:1172px">$ 3400</p>
</main>
</body>
</html>
```